Adult Flushable Wipes Product Packaging design

We are launching an adult flushable wipe and we require a logo & product packaging design.

The brand is called: Velvet Valet

The wipe will be slightly upmarket and will sell mainly online. The branding should be funny but still professional. It's intended audience is men between 18-45 and it will be used as a body cleansing wipe.

for general body cleaning
-bathroom/toilet wipes
-grooming wipes
-refreshing wipes

Target Market(s)

Men Ages 18-45

Font styles to use
Decorative

Colors
86cfc6
33b8a4
85cae6
33a6d7

Requirements
Must have
• there are 50 wipes per pack. this should be incorporated in the design.
• the wipes are 5.9" x 7.9" this should be incorporated in the design.
• the wipes have a fragrance which we will call the "Velvet Breeze" this should be incorporated in the design.
Nice to have
• We like the idea of incorporating a butler/tuxedo into the product design. lots of black/white with a matte finish and can also have some silver.
Should not have
• too many colours. we want a simple design

```html
<!DOCTYPE html>
<html lang="en">
<head>
<meta charset="utf-8">
<title>Velvet Valet Flushable Wipe – Pack Front</title>
<link rel="stylesheet" href="https://fonts.googleapis.com/css2?family=Chewy&family=Cinzel:wght@500&family=Montserrat:wght@700;800&family=Oswald:wght@700&display=swap">
<style>
  :root {
    --backdrop: #70587c;
    --pack-black: #111111;
    --pack-charcoal: #1c1c1c;
    --silver-light: #e6e6e6;
    --silver-mid: #a9a9a9;
    --silver-dark: #6f6f6f;
    --paper-white: #f2f2f2;
    --ink: #1a1a1a;
    --white: #ffffff;
  }
  html, body {
    margin: 0;
    padding: 0;
    width: 1200px;
    height: 921px;
    overflow: hidden;
    background: var(--backdrop);
  }
  .canvas {
    display: block;
    width: 1200px;
    height: 921px;
  }
  .brand-name {
    font-family: "Oswald", sans-serif;
    font-weight: 700;
    font-size: 54px;
    fill: var(--white);
    letter-spacing: 1px;
  }
  .product-type {
    font-family: "Chewy", cursive;
    font-size: 32px;
    fill: var(--white);
    stroke: var(--ink);
    stroke-width: 5px;
    paint-order: stroke;
    letter-spacing: 0.5px;
  }
  .fragrance {
    font-family: "Cinzel", serif;
    font-weight: 500;
    font-size: 19.5px;
    fill: var(--ink);
    letter-spacing: 0.8px;
  }
  .use-list {
    font-family: "Montserrat", sans-serif;
    font-weight: 700;
    font-size: 12.6px;
    fill: var(--ink);
    letter-spacing: 0.3px;
  }
  .badge-big {
    font-family: "Montserrat", sans-serif;
    font-weight: 800;
    font-size: 9px;
    fill: var(--white);
  }
  .badge-small {
    font-family: "Montserrat", sans-serif;
    font-weight: 700;
    font-size: 5px;
    fill: var(--white);
  }
</style>
</head>
<body>
<svg class="canvas" viewBox="0 0 1200 921" xmlns="http://www.w3.org/2000/svg">
  <defs>
    <linearGradient id="silverBand" x1="0" y1="0" x2="1" y2="0">
      <stop offset="0" stop-color="var(--silver-dark)"/>
      <stop offset="0.5" stop-color="var(--silver-light)"/>
      <stop offset="1" stop-color="var(--silver-dark)"/>
    </linearGradient>
    <radialGradient id="emblemTone" cx="0.5" cy="0.45" r="0.6">
      <stop offset="0" stop-color="var(--white)"/>
      <stop offset="1" stop-color="var(--silver-mid)"/>
    </radialGradient>
    <clipPath id="packClip">
      <rect x="152" y="248" width="898" height="428"/>
    </clipPath>
  </defs>

  <!-- pack face -->
  <g class="pack" clip-path="url(#packClip)">
    <rect class="pack-body" x="152" y="248" width="898" height="428" fill="var(--pack-black)"/>

    <!-- silver sweep and white lower panel -->
    <path class="silver-sweep" d="M152 612 Q601 448 1050 612 L1050 676 L152 676 Z" fill="url(#silverBand)"/>
    <path class="white-panel" d="M152 624 Q601 464 1050 624 L1050 676 L152 676 Z" fill="var(--paper-white)"/>
  </g>

  <!-- count badge -->
  <g class="badge badge-count">
    <circle cx="266" cy="328" r="30" fill="var(--pack-black)" stroke="var(--white)" stroke-width="2.5"/>
    <g fill="var(--white)" stroke="var(--pack-black)" stroke-width="1">
      <path d="M252 322 L276 322 L282 316 L258 316 Z"/>
      <path d="M252 326 L276 326 L282 320 L258 320 Z"/>
      <path d="M252 330 L276 330 L282 324 L258 324 Z"/>
    </g>
    <text class="badge-big" x="266" y="343" text-anchor="middle">50 WIPES</text>
    <text class="badge-small" x="266" y="350" text-anchor="middle">PER PACK</text>
  </g>

  <!-- size badge -->
  <g class="badge badge-size">
    <circle cx="956" cy="328" r="30" fill="var(--pack-black)" stroke="var(--white)" stroke-width="2.5"/>
    <text class="badge-small" x="956" y="309" text-anchor="middle">WIPES SIZE</text>
    <g stroke="var(--white)" stroke-width="1.8" fill="none">
      <path d="M950 320 L944 314 M944 314 L944 318 M944 314 L948 314"/>
      <path d="M962 320 L968 314 M968 314 L968 318 M968 314 L964 314"/>
      <path d="M950 326 L944 332 M944 332 L944 328 M944 332 L948 332"/>
      <path d="M962 326 L968 332 M968 332 L968 328 M968 332 L964 332"/>
    </g>
    <text class="badge-big" x="956" y="344" text-anchor="middle" font-size="8">5.9" X 7.9"</text>
  </g>

  <!-- emblem illustration area -->
  <rect class="flourish" x="455" y="392" width="105" height="40" rx="20" fill="var(--silver-dark)" opacity="0.55" role="img" aria-label="Silver scroll ornament"/>
  <rect class="flourish" x="670" y="392" width="105" height="40" rx="20" fill="var(--silver-dark)" opacity="0.55" role="img" aria-label="Silver scroll ornament"/>
  <circle class="mascot" cx="615" cy="368" r="50" fill="url(#emblemTone)" stroke="var(--silver-mid)" stroke-width="4" role="img" aria-label="Illustration of a smiling butler in a tuxedo and bow tie"/>

  <!-- brand name -->
  <text class="brand-name" x="601" y="506" text-anchor="middle">VELVET VALET</text>

  <!-- product line -->
  <line x1="468" y1="570" x2="502" y2="570" stroke="var(--ink)" stroke-width="2"/>
  <line x1="706" y1="570" x2="740" y2="570" stroke="var(--ink)" stroke-width="2"/>
  <text class="product-type" x="604" y="578" text-anchor="middle">Flushable Wipe</text>

  <line x1="430" y1="590" x2="802" y2="590" stroke="var(--ink)" stroke-width="1"/>
  <text class="fragrance" x="608" y="611" text-anchor="middle">VELVET BREEZE FRAGRANCE</text>
  <line x1="430" y1="619" x2="802" y2="619" stroke="var(--ink)" stroke-width="1"/>

  <text class="use-list" x="613" y="655" text-anchor="middle">FOR GENERAL BODY CLEANING: BATHROOM/TOILET WIPES | GROOMING WIPES | REFRESHING WIPES</text>
</svg>
</body>
</html>
```